Business Card for Beach theme sports bar called TAVRU

I need a business card designed for our employees, front and back. This will be used by the employees of two business locations to hand out to customers. I've attached the previous business cards we used at one time for a Benwicks (it is now Tavru). Looking for a fresh new card that is elegant but has character.

Target Market(s)

30-60, middle class

Contact Information for Business Card

We are a beach bar and sports bar. I am looking for an elegant business card with the front to have the TAVRU logo. Then on the back I need it to allow a space for employees to write their names and for them to write in their schedule. I have attached our old cards with our old name Benwicks so you can pull everything we need on the cards. one thing is missing is we have another location at 2815 N Willow Crest Rd with a number of 702-418-9351. Since we will use it for both locations it should allow the employee to circle or check mark the bar which they work at.

Font styles to use
Sans Serif

Requirements
Must have
• We are looking for some fresh ideas for the business card. Something that will really stick out to customers when the staff hands them out. Creativity will be looked at positively, but we still want it to look upscale and fun.

```html
<!DOCTYPE html>
<html lang="en">
<head>
<meta charset="UTF-8">
<title>Tavru Business Card</title>
<link href="https://fonts.googleapis.com/css2?family=Oswald:wght@500&family=Work+Sans:wght@400;500&display=swap" rel="stylesheet">
<style>
  :root {
    --backdrop: #151515;
    --card: #1e1e1e;
    --card-edge: #262626;
    --ink: #f2f2f2;
    --silver: #b9b9b9;
    --muted: #bdbdbd;
    --rule: #8a8a8a;
  }
  * { margin: 0; padding: 0; box-sizing: border-box; }
  html, body {
    width: 1200px;
    height: 900px;
    overflow: hidden;
    background: var(--backdrop);
  }
  .canvas {
    width: 1200px;
    height: 900px;
    display: flex;
    flex-direction: column;
    align-items: center;
    justify-content: center;
    gap: 40px;
  }
  .card {
    position: relative;
    width: 640px;
    height: 366px;
    background: linear-gradient(135deg, var(--card) 0%, var(--card-edge) 100%);
    box-shadow: 0 12px 30px rgba(0,0,0,0.55);
  }

  /* Front */
  .card-front {
    display: flex;
    align-items: center;
    justify-content: center;
  }
  .brand {
    display: flex;
    align-items: center;
    gap: 14px;
  }
  .brand-dot {
    width: 18px;
    height: 18px;
    border-radius: 50%;
    background: var(--silver);
  }
  .brand-name {
    font-family: "Work Sans", sans-serif;
    font-weight: 500;
    font-size: 54px;
    letter-spacing: 6px;
    color: var(--silver);
  }

  /* Back */
  .identity {
    position: absolute;
    left: 40px;
    top: 36px;
    width: 330px;
    text-align: right;
  }
  .identity-title {
    font-family: "Oswald", sans-serif;
    font-weight: 500;
    font-size: 30px;
    letter-spacing: 1.5px;
    line-height: 34px;
    color: var(--ink);
  }
  .write-line {
    display: block;
    margin-left: auto;
    margin-top: 22px;
    width: 240px;
    height: 1px;
    background: var(--rule);
  }
  .write-label {
    font-family: "Work Sans", sans-serif;
    font-size: 12px;
    line-height: 16px;
    margin-top: 5px;
    color: var(--muted);
  }
  .divider {
    position: absolute;
    left: 392px;
    top: 44px;
    width: 2px;
    height: 66px;
    background: var(--ink);
  }
  .contact-list {
    position: absolute;
    left: 414px;
    top: 40px;
    list-style: none;
    font-family: "Work Sans", sans-serif;
    font-size: 16px;
    color: var(--ink);
    letter-spacing: 0.5px;
  }
  .contact-list li {
    display: flex;
    align-items: center;
    gap: 10px;
    height: 25px;
  }
  .contact-list svg {
    width: 11px;
    height: 11px;
    fill: none;
    stroke: var(--ink);
    stroke-width: 1.6;
  }

  .schedule {
    position: absolute;
    left: 40px;
    top: 150px;
    width: 560px;
  }
  .section-label {
    font-family: "Work Sans", sans-serif;
    font-weight: 500;
    font-size: 12px;
    letter-spacing: 2px;
    line-height: 16px;
    color: var(--muted);
  }
  .schedule-days {
    display: grid;
    grid-template-columns: repeat(7, 1fr);
    gap: 10px;
    margin-top: 10px;
    list-style: none;
  }
  .schedule-days li {
    height: 46px;
    border-bottom: 1px solid var(--rule);
    font-family: "Work Sans", sans-serif;
    font-size: 12px;
    color: var(--ink);
    letter-spacing: 1px;
  }

  .locations {
    position: absolute;
    left: 40px;
    bottom: 32px;
    list-style: none;
    font-family: "Work Sans", sans-serif;
    font-size: 15px;
    letter-spacing: 0.4px;
    color: var(--ink);
  }
  .locations li {
    display: flex;
    align-items: center;
    gap: 12px;
    height: 28px;
  }
  .check-box {
    width: 14px;
    height: 14px;
    border: 1.5px solid var(--ink);
    flex: none;
  }
  .location-phone { color: var(--muted); }
</style>
</head>
<body>
<main class="canvas">
  <section class="card card-front">
    <div class="brand">
      <span class="brand-dot"></span>
      <span class="brand-name">TAVRU</span>
    </div>
  </section>

  <section class="card card-back">
    <div class="identity">
      <p class="identity-title">YOUR HOST</p>
      <span class="write-line"></span>
      <p class="write-label">Name</p>
    </div>
    <span class="divider"></span>
    <ul class="contact-list">
      <li>
        <svg viewBox="0 0 12 12"><path d="M3 1 L5 3.5 L4 5 Q5 7.5 7 8 L8.5 7 L11 9 L9.5 11 Q3 10 1 2.5 Z"/></svg>
        (514) 630-7125
      </li>
      <li>
        <svg viewBox="0 0 12 12"><rect x="1" y="2.5" width="10" height="7"/><path d="M1 2.5 L6 6.5 L11 2.5"/></svg>
        info@tavru.com
      </li>
      <li>
        <svg viewBox="0 0 12 12"><circle cx="6" cy="6" r="5"/><ellipse cx="6" cy="6" rx="2.2" ry="5"/><path d="M1 6 H11"/></svg>
        www.tavru.com
      </li>
    </ul>

    <div class="schedule">
      <p class="section-label">MY SCHEDULE</p>
      <ul class="schedule-days">
        <li>MON</li><li>TUE</li><li>WED</li><li>THU</li><li>FRI</li><li>SAT</li><li>SUN</li>
      </ul>
    </div>

    <ul class="locations">
      <li><span class="check-box"></span>418b Marlow Street, Ashcombe, NZ, 8042 <span class="location-phone">(514) 630-7125</span></li>
      <li><span class="check-box"></span>2815 N Willow Crest Rd <span class="location-phone">702-418-9351</span></li>
    </ul>
  </section>
</main>
</body>
</html>
```